Pediatric Dentist Business Card

I need a business card designed for a dentist who works exclusively with children.
We prefer designs that are out of ordiary that is fun and interesting to kids.

there is no logo since this is a dentists office. The name of the doctor is "Tavor Kesh" if you want to get creative with that.

Target Market(s)

Kids

Industry/Entity Type

Business

Contact Information for Business Card

Anythings that is creative

Colors

Designer to choose colors to be used in the design.

```html
<!DOCTYPE html>
<html lang="en">
<head>
<meta charset="utf-8">
<title>Tavor Kesh – Business Card</title>
<link href="https://fonts.googleapis.com/css2?family=Fredoka:wght@500;600&family=Nunito:wght@600;700&display=swap" rel="stylesheet">
<style>
  :root{
    --page:#e9eaee;
    --sky:#33b4ef;
    --blue:#3a6fe0;
    --indigo:#3b33a8;
    --ink:#1f2033;
    --name:#34354a;
    --title:#2f96e0;
    --white:#ffffff;
  }
  *{margin:0;padding:0;box-sizing:border-box}
  html,body{width:1200px;height:900px;overflow:hidden;background:var(--page)}
  .canvas{position:relative;width:1200px;height:900px}
  .card{position:absolute;width:560px;height:320px;border-radius:22px;overflow:hidden;box-shadow:0 10px 28px rgba(0,0,0,.18)}

  /* back side */
  .card-back{left:80px;top:110px;background:linear-gradient(100deg,var(--sky) 0%,var(--blue) 45%,var(--indigo) 100%)}
  .brand{position:absolute;left:0;right:0;top:56px;display:flex;flex-direction:column;align-items:center;gap:14px}
  .brand-circle{width:104px;height:104px;border-radius:50%;background:var(--white)}
  .brand-name{font-family:'Fredoka',sans-serif;font-weight:600;font-size:22px;letter-spacing:1px;color:var(--white)}
  .back-strip{position:absolute;left:0;right:0;bottom:0;height:52px;background:var(--white);display:flex;align-items:center;justify-content:space-around;padding:0 12px}

  .contact{display:flex;align-items:center;gap:8px;font-family:'Nunito',sans-serif;font-weight:700;font-size:12.5px;color:var(--ink);white-space:nowrap}
  .icon{width:20px;height:20px;flex:none}

  /* front side */
  .card-front{left:560px;top:470px;background:var(--white)}
  .front-colour{position:absolute;inset:0;width:560px;height:320px}
  .identity{position:absolute;left:232px;top:52px;display:flex;align-items:center;gap:14px}
  .identity-circle{width:70px;height:70px;border-radius:50%;background:linear-gradient(135deg,var(--sky),var(--indigo));flex:none}
  .name{font-family:'Fredoka',sans-serif;font-weight:600;font-size:28px;color:var(--name);letter-spacing:.5px;line-height:1}
  .role{font-family:'Nunito',sans-serif;font-weight:700;font-size:15px;color:var(--title);margin-top:4px}
  .front-contacts{position:absolute;left:330px;top:148px;list-style:none;display:flex;flex-direction:column;gap:13px}
  .front-contacts .contact{font-size:14px;gap:12px}
  .front-contacts .icon{width:24px;height:24px}
</style>
</head>
<body>
<div class="canvas">

  <section class="card card-back" aria-label="Business card back">
    <div class="brand">
      <div class="brand-circle"></div>
      <span class="brand-name">Kesh Kids Dental</span>
    </div>
    <div class="back-strip">
      <span class="contact">
        <svg class="icon" viewBox="0 0 20 20"><circle cx="10" cy="10" r="10" fill="#1f2033"/><rect x="5" y="6.5" width="10" height="7" rx="1" fill="#fff"/><path d="M5.5 7l4.5 3.5L14.5 7" stroke="#1f2033" stroke-width="1.2" fill="none"/></svg>
        hello@tavorkesh.com
      </span>
      <span class="contact">
        <svg class="icon" viewBox="0 0 20 20"><circle cx="10" cy="10" r="10" fill="#1f2033"/><circle cx="10" cy="10" r="6" stroke="#fff" stroke-width="1.3" fill="none"/><ellipse cx="10" cy="10" rx="2.6" ry="6" stroke="#fff" stroke-width="1.2" fill="none"/><path d="M4 10h12" stroke="#fff" stroke-width="1.2"/></svg>
        www.tavorkesh.com
      </span>
      <span class="contact">
        <svg class="icon" viewBox="0 0 20 20"><circle cx="10" cy="10" r="10" fill="#3b33a8"/><path d="M10 15s-4-4.2-4-7a4 4 0 018 0c0 2.8-4 7-4 7z" fill="#fff"/><circle cx="10" cy="8" r="1.5" fill="#3b33a8"/></svg>
        Maple Lane 12, Brookford
      </span>
    </div>
  </section>

  <section class="card card-front" aria-label="Business card front">
    <svg class="front-colour" viewBox="0 0 560 320" role="img" aria-label="Decorative layered blue wave artwork">
      <defs>
        <linearGradient id="frontGradient" x1="0" y1="0" x2="1" y2="1">
          <stop offset="0" stop-color="#33b4ef"/><stop offset="1" stop-color="#3b33a8"/>
        </linearGradient>
      </defs>
      <path d="M0 0 H170 C110 90 170 250 340 300 C420 322 480 320 560 310 V320 H0Z" fill="url(#frontGradient)"/>
    </svg>
    <div class="identity">
      <div class="identity-circle"></div>
      <div>
        <h1 class="name">Tavor Kesh</h1>
        <p class="role">Dentist</p>
      </div>
    </div>
    <ul class="front-contacts">
      <li class="contact">
        <svg class="icon" viewBox="0 0 20 20"><circle cx="10" cy="10" r="10" fill="#1f2033"/><rect x="5" y="6.5" width="10" height="7" rx="1" fill="#fff"/><path d="M5.5 7l4.5 3.5L14.5 7" stroke="#1f2033" stroke-width="1.2" fill="none"/></svg>
        hello@tavorkesh.com
      </li>
      <li class="contact">
        <svg class="icon" viewBox="0 0 20 20"><circle cx="10" cy="10" r="10" fill="#1f2033"/><path d="M7 5.5l1.8 2.3-1 1.3c.6 1.3 1.7 2.4 3 3l1.3-1 2.3 1.8-1 1.6c-3.6-.2-7.4-4-7.6-7.6z" fill="#fff"/></svg>
        555 010 2468
      </li>
      <li class="contact">
        <svg class="icon" viewBox="0 0 20 20"><circle cx="10" cy="10" r="10" fill="#3b33a8"/><path d="M10 15s-4-4.2-4-7a4 4 0 018 0c0 2.8-4 7-4 7z" fill="#fff"/><circle cx="10" cy="8" r="1.5" fill="#3b33a8"/></svg>
        Maple Lane 12, Brookford
      </li>
      <li class="contact">
        <svg class="icon" viewBox="0 0 20 20"><circle cx="10" cy="10" r="10" fill="#1f2033"/><circle cx="10" cy="10" r="6" stroke="#fff" stroke-width="1.3" fill="none"/><ellipse cx="10" cy="10" rx="2.6" ry="6" stroke="#fff" stroke-width="1.2" fill="none"/><path d="M4 10h12" stroke="#fff" stroke-width="1.2"/></svg>
        www.tavorkesh.com
      </li>
    </ul>
  </section>

</div>
</body>
</html>
```